Business cards design on a high standard

We advise clients on insurance and financial matters, since these clients pay for our advice, the design should have a high standard. Our logo should be included. From the colors we are open for everything.

Colors

Designer to choose colors to be used in the design.

```html
<!DOCTYPE html>
<html lang="en">
<head>
<meta charset="utf-8">
<title>Lumen Advisory – Business Cards</title>
<link rel="stylesheet" href="https://fonts.googleapis.com/css2?family=Lato:wght@400;700;900&display=swap">
<style>
  :root {
    --brand-red: #dc0000;
    --paper: #ffffff;
    --frost: #e6e3e3;
    --frost-edge: #d3cfcf;
    --stage: #eeeceb;
    --ink-light: #ffffff;
  }
  * { box-sizing: border-box; margin: 0; padding: 0; }
  html, body {
    width: 1200px; height: 900px; overflow: hidden;
    background: var(--stage);
    font-family: "Lato", Arial, sans-serif;
  }
  .canvas { position: relative; width: 1200px; height: 900px; }

  .card {
    position: absolute; width: 526px; height: 326px;
    overflow: hidden;
    box-shadow: 0 10px 30px rgba(0,0,0,.12);
  }
  .card--front { left: 224px; top: 106px;
    background: linear-gradient(90deg, var(--brand-red) 0 356px, var(--paper) 356px 100%); }
  .card--back { left: 427px; top: 478px;
    background: linear-gradient(90deg, var(--paper) 0 170px, var(--brand-red) 170px 100%); }

  .frost-disc {
    position: absolute; width: 282px; height: 282px; border-radius: 50%;
    background: radial-gradient(circle at 50% 45%, #efeded 0%, var(--frost) 65%, var(--frost-edge) 100%);
    box-shadow: inset 0 0 10px rgba(0,0,0,.08);
    display: flex; align-items: center; justify-content: center;
  }
  .card--front .frost-disc { left: 218px; top: 22px; }
  .card--back .frost-disc { left: 17px; top: 22px; }

  .wordmark {
    display: block; text-align: center;
    font-weight: 900; text-transform: uppercase; letter-spacing: 2px;
    white-space: nowrap; line-height: 1.05;
  }
  .wordmark--disc { color: var(--brand-red); font-size: 30px; }
  .wordmark--ghost { color: rgba(220,0,0,.35); font-size: 30px; transform: scaleX(-1); }
  .wordmark--back {
    position: absolute; left: 318px; top: 128px; width: 186px;
    color: var(--ink-light); font-size: 24px;
  }

  .holder { position: absolute; left: 31px; top: 33px; color: var(--ink-light); }
  .holder__name { font-size: 17px; font-weight: 700; letter-spacing: .3px; line-height: 22px; }
  .holder__role { font-size: 14px; line-height: 18px; }

  .contact-list {
    position: absolute; left: 31px; top: 178px; list-style: none;
    color: var(--ink-light); font-size: 14px; line-height: 19px;
  }
  .contact-list li { display: flex; align-items: center; gap: 5px; white-space: nowrap; }
  .contact-list svg { width: 11px; height: 11px; fill: var(--ink-light); flex: none; }

  .address {
    position: absolute; left: 33px; top: 250px;
    color: var(--ink-light); font-size: 14px; line-height: 19px; font-style: normal;
  }

  .web-back {
    position: absolute; left: 318px; top: 199px; width: 186px; text-align: center;
    color: var(--ink-light); font-size: 14px; white-space: nowrap;
  }
</style>
</head>
<body>
<main class="canvas">

  <section class="card card--front" aria-label="Business card front">
    <div class="holder">
      <p class="holder__name">DANIEL WHITMORE</p>
      <p class="holder__role">Managing Director</p>
    </div>

    <ul class="contact-list">
      <li>
        <svg viewBox="0 0 12 12" aria-hidden="true"><path d="M1 4c0-2 1-3 5-3s5 1 5 3l-2 1-1-2H4L3 5zM3 6h6l1 5H2z"/></svg>
        044-555 010 234
      </li>
      <li>
        <svg viewBox="0 0 12 12" aria-hidden="true"><path d="M1 2h10v8H1zM1.8 3v.4L6 6.4l4.2-3V3L6 5.6z" fill-rule="evenodd"/></svg>
        info@lumenadvisory.com
      </li>
      <li>
        <svg viewBox="0 0 12 12" aria-hidden="true"><circle cx="6" cy="6" r="5"/></svg>
        www.lumenadvisory.com
      </li>
    </ul>

    <address class="address">421, Address line here,<br>45452,Country Name</address>

    <div class="frost-disc">
      <span class="wordmark wordmark--disc">Lumen<br>Advisory</span>
    </div>
  </section>

  <section class="card card--back" aria-label="Business card back">
    <div class="frost-disc">
      <span class="wordmark wordmark--ghost" aria-hidden="true">Lumen<br>Advisory</span>
    </div>
    <span class="wordmark wordmark--back">Lumen<br>Advisory</span>
    <p class="web-back">www.lumenadvisory.com</p>
  </section>

</main>
</body>
</html>
```